Crazy, Different WOMENS PREWORKOUT Packaging Label

We need a MODERN, CRAZY, FUN packaging preworkout label for WOMEN.
There are no limits for this project, be wild and crazy and DIFFERENT.

The name of the product is VELTANE BLUSH and it is a gym preworkout supplement for women.
The company is called KORVAPLENTIX.

We're looking to convey strength, femininity, uniqueness, health, vitality, vigor, focus, concentration, energy, stamina.

and above all HEALTH
Updates

Project Deadline Extended Reason: Hello All, thanks for your submissions so far. In the interest of receiving the best designs, we will extend the deadline by 5 days. We appreciate your effort and look forward to further revisions to hone and perfect the concepts already submitted. Thank you all for your effort so far! Added Saturday, January 7, 2017

Target Market(s)

Sports Women and Women Gym goers

Font styles to use
Serif
Sans Serif
Decorative
Other font styles liked:
• AR Destine

Requirements
Must have
• It must have SOME red in it somewhere because the product is called VELTANE BLUSH but it does NOT have to be the dominating color.
• It must include our Company logo on the label too, but the company logo and the product name should be harmonious. It should be obvious which part of the design is the company logo and which part is the name of the product.
• Include any one of the Company Logo Strips on the label (see reference files) can make it any color!
Nice to have
• Nice to have something unique and different but appealing to women. but NOT stereotypical of women...
• It should be something strong, elite and feminine BUT NOT bubblegum pink and rainbows...
• The jar is a round white jar.
• Try make it look clean, healthful, effective.
• I'm open to crazy and simple designs.
Should not have
• Should not JUST be pink and purple and stereotypical to women.
• It CAN have pink and purple in it though.

```html
<!DOCTYPE html>
<html lang="en">
<head>
<meta charset="utf-8">
<title>Veltane Blush – Preworkout Label</title>
<link rel="stylesheet" href="https://fonts.googleapis.com/css2?family=Oswald:wght@300;400;700&family=Orbitron:wght@500;700&display=swap">
<style>
  :root {
    --red-deep: #b30a0c;
    --red-main: #d0141a;
    --red-bright: #ff1018;
    --red-soft: #ef8a7c;
    --ink: #0b0b0b;
    --paper: #ffffff;
  }
  html, body {
    margin: 0;
    padding: 0;
    width: 1200px;
    height: 905px;
    overflow: hidden;
    background: var(--paper);
  }
  .label {
    position: relative;
    width: 1200px;
    height: 905px;
    overflow: hidden;
    background: var(--paper);
  }
  .label-art {
    position: absolute;
    inset: 0;
    width: 1200px;
    height: 905px;
  }
  .tagline {
    position: absolute;
    left: 77px;
    top: 150px;
    margin: 0;
    font-family: "Oswald", sans-serif;
    font-weight: 300;
    font-size: 58px;
    line-height: 57px;
    letter-spacing: 0.5px;
    color: var(--paper);
    text-transform: uppercase;
  }
  .brand {
    position: absolute;
    left: 300px;
    top: 420px;
    display: flex;
    align-items: center;
    gap: 18px;
  }
  .brand-square {
    width: 44px;
    height: 44px;
    background: var(--ink);
  }
  .brand-name {
    font-family: "Oswald", sans-serif;
    font-weight: 700;
    font-size: 64px;
    letter-spacing: 3px;
    color: var(--ink);
    line-height: 1;
  }
  .product-name {
    position: absolute;
    right: 50px;
    top: 660px;
    margin: 0;
    text-align: right;
    font-family: "Orbitron", sans-serif;
    font-style: normal;
    transform: skewX(-10deg);
  }
  .product-name .line-top {
    display: block;
    font-weight: 500;
    font-size: 64px;
    letter-spacing: 2px;
    color: var(--ink);
    line-height: 1.1;
  }
  .product-name .line-main {
    display: block;
    font-weight: 700;
    font-size: 108px;
    letter-spacing: 2px;
    color: var(--red-main);
    line-height: 1.05;
  }
</style>
</head>
<body>
<main class="label">
  <svg class="label-art" viewBox="0 0 1200 905" xmlns="http://www.w3.org/2000/svg" aria-hidden="false">
    <defs>
      <linearGradient id="redField" x1="0" y1="0" x2="1" y2="0">
        <stop offset="0" stop-color="var(--red-main)"/>
        <stop offset="0.55" stop-color="var(--red-deep)"/>
        <stop offset="1" stop-color="var(--red-soft)"/>
      </linearGradient>
      <linearGradient id="swooshTone" x1="0" y1="1" x2="1" y2="0">
        <stop offset="0" stop-color="#e04a44"/>
        <stop offset="0.7" stop-color="#f2a79d"/>
        <stop offset="1" stop-color="#ffffff"/>
      </linearGradient>
      <linearGradient id="lowerTone" x1="0" y1="0" x2="1" y2="1">
        <stop offset="0" stop-color="#d62a28"/>
        <stop offset="1" stop-color="#e8675d"/>
      </linearGradient>
      <linearGradient id="sprigTone" x1="0" y1="0" x2="0" y2="1">
        <stop offset="0" stop-color="#e9605a"/>
        <stop offset="1" stop-color="#f7c9c3"/>
      </linearGradient>
    </defs>

    <rect class="red-field" x="0" y="0" width="1200" height="905" fill="url(#redField)"/>

    <path class="lined-lower" role="img" aria-label="Fine diagonal line pattern in light red"
          d="M0,540 Q600,430 1200,90 L1200,620 Q560,680 0,800 Z" fill="url(#lowerTone)"/>

    <path class="swoosh-band" role="img" aria-label="Sweeping band of fine white lines rising to the upper right"
          d="M0,545 Q620,420 1200,80 L1200,0 L1100,0 Q650,300 0,440 Z" fill="url(#swooshTone)"/>

    <circle class="swoosh-glow" cx="1085" cy="25" r="28" fill="var(--paper)"/>

    <path class="leaf-sprigs" role="img" aria-label="Row of white leaf sprigs along the lower left"
          d="M0,700 Q200,690 500,860 L500,905 L0,905 Z" fill="url(#sprigTone)"/>

    <path class="white-base" d="M0,830 Q520,720 1200,540 L1200,905 L0,905 Z" fill="var(--paper)"/>
  </svg>

  <p class="tagline">Gym preworkout<br>supplement<br>for women</p>

  <div class="brand">
    <span class="brand-square"></span>
    <span class="brand-name">KORVAPLENTIX</span>
  </div>

  <h1 class="product-name">
    <span class="line-top">VELTANE</span>
    <span class="line-main">BLUSH</span>
  </h1>
</main>
</body>
</html>
```